Wanderlark Gin - Bottle Label for a craft Gin about to be launched on the world from New Zealand

We are a start up craft distillery in New Zealand. We have developed a wonderful Gin using our own grain spirit and both traditional and New Zealand native botanicals (Manuka to be specific), chosen our bottle and the name "Wanderlark" and done a bit of amateur label design and now we are looking for someone to make it great.

Feel free to change up our amateur concept but give us something that will pop from the back bar and scream authenticity, craft and individuality.

The attached files give you the specifications of the bottle, our current concept for a Wanderlark label and an earlier concept drawing that gives an idea of where we are thinking the two labels should go on the front of the bottle.

Thanks, we look forward to your ideas!!

Target Market(s)

High end and craft Gin drinkers. Hipsters and cocktail barflys and their bar tenders and bar owners

Requirements
Must have
• Attractive individuality
Nice to have
• Coolness
Should not have
• Uncoolness

```html
<!DOCTYPE html>
<html lang="en">
<head>
<meta charset="utf-8">
<title>Wanderlark Gin – Wild Meadow Label</title>
<link rel="stylesheet" href="https://fonts.googleapis.com/css2?family=Kaushan+Script&family=Libre+Baskerville&family=Cinzel:wght@400;700;900&family=Roboto:wght@700&display=swap">
<style>
  :root {
    --canvas: #ffffff;
    --gold-light: #f6c76a;
    --gold-mid: #e09a2c;
    --gold-deep: #b86d14;
    --cream: #fdf9b0;
    --cream-edge: #f2e88a;
    --wine: #8e1020;
    --wine-dark: #6a0a16;
    --ink: #2a1a0c;
    --blossom: #f3c6dc;
    --blossom-deep: #c9799f;
    --leaf: #4f6b2e;
  }
  html, body {
    margin: 0;
    padding: 0;
    width: 1029px;
    height: 1200px;
    overflow: hidden;
    background: var(--canvas);
  }
  .canvas {
    position: relative;
    width: 1029px;
    height: 1200px;
  }
  .shape-layer {
    position: absolute;
    inset: 0;
  }
  .text {
    position: absolute;
    left: 0;
    width: 1029px;
    text-align: center;
    margin: 0;
    white-space: nowrap;
  }

  /* Front label */
  .brand-name {
    top: 104px;
    font-family: "Cinzel", serif;
    font-weight: 700;
    font-size: 24px;
    line-height: 30px;
    letter-spacing: 2px;
    color: var(--cream);
  }
  .product-name {
    top: 300px;
    font-family: "Kaushan Script", cursive;
    font-weight: 400;
    font-size: 96px;
    line-height: 110px;
    color: var(--wine);
  }
  .product-type {
    top: 424px;
    font-family: "Libre Baskerville", serif;
    font-weight: 400;
    font-size: 36px;
    line-height: 44px;
    letter-spacing: 1px;
    color: var(--wine-dark);
  }
  .volume {
    top: 612px;
    font-family: "Roboto", sans-serif;
    font-weight: 700;
    font-size: 40px;
    line-height: 48px;
    color: var(--wine);
  }

  /* Recipe label */
  .recipe-title {
    top: 784px;
    font-family: "Libre Baskerville", serif;
    font-weight: 400;
    font-size: 50px;
    line-height: 64px;
    color: var(--ink);
  }
  .recipe-notes {
    top: 873px;
    font-family: "Cinzel", serif;
    font-weight: 900;
    font-size: 24px;
    line-height: 35px;
    color: var(--ink);
  }
  .strength {
    top: 1068px;
    font-family: "Cinzel", serif;
    font-weight: 900;
    font-size: 24px;
    line-height: 32px;
    color: var(--ink);
  }
</style>
</head>
<body>
<main class="canvas">
  <svg class="shape-layer" width="1029" height="1200" viewBox="0 0 1029 1200">
    <defs>
      <linearGradient id="gold-frame" x1="0" y1="0" x2="1" y2="1">
        <stop offset="0" stop-color="#f6c76a"/>
        <stop offset="0.45" stop-color="#e09a2c"/>
        <stop offset="1" stop-color="#b86d14"/>
      </linearGradient>
      <linearGradient id="gold-band" x1="0" y1="0" x2="1" y2="0">
        <stop offset="0" stop-color="#b86d14"/>
        <stop offset="0.5" stop-color="#f6c76a"/>
        <stop offset="1" stop-color="#b86d14"/>
      </linearGradient>
      <radialGradient id="blossom-fill" cx="0.5" cy="0.5" r="0.6">
        <stop offset="0" stop-color="#f3c6dc"/>
        <stop offset="0.7" stop-color="#c9799f"/>
        <stop offset="1" stop-color="#4f6b2e" stop-opacity="0.35"/>
      </radialGradient>
    </defs>

    <g class="front-label">
      <rect x="177" y="60" width="680" height="634" rx="80" fill="url(#gold-frame)" stroke="#b86d14" stroke-width="4"/>
      <rect x="272" y="150" width="495" height="435" rx="60" fill="#fdf9b0" stroke="#f2e88a" stroke-width="3"/>

      <rect x="388" y="94" width="252" height="52" rx="26" fill="#8e1020" stroke="#fdf9b0" stroke-width="4"/>

      <ellipse cx="514" cy="72" rx="56" ry="18" fill="url(#blossom-fill)" role="img" aria-label="Small manuka blossom ornament above the brand plate"/>
      <ellipse cx="262" cy="215" rx="80" ry="88" fill="url(#blossom-fill)" role="img" aria-label="Cluster of pink manuka blossoms with green leaves"/>
      <ellipse cx="772" cy="565" rx="78" ry="86" fill="url(#blossom-fill)" role="img" aria-label="Cluster of pink manuka blossoms with green leaves"/>
    </g>

    <g class="recipe-label">
      <polygon points="300,742 730,742 790,800 790,1140 735,1195 295,1195 240,1140 240,800" fill="#e09a2c"/>
      <polygon points="306,752 724,752 780,806 780,1134 729,1185 301,1185 250,1134 250,806" fill="#fdf9b0"/>
      <rect x="300" y="776" width="430" height="80" fill="url(#gold-band)" stroke="#b86d14" stroke-width="2"/>
    </g>
  </svg>

  <p class="text brand-name">WANDERLARK</p>
  <h1 class="text product-name">Wild Meadow</h1>
  <p class="text product-type">SMALL BATCH GIN</p>
  <p class="text volume">500 ml</p>

  <h2 class="text recipe-title">RECIPE #3</h2>
  <p class="text recipe-notes">REFRESHING BLEND OF<br>GIN BOTANICALS INCLUDING<br>ORGANIC MANUKA BARK<br>FROM STEWART ISLAND<br>FOR FLAVOUR</p>
  <p class="text strength">ABV 421</p>
</main>
</body>
</html>
```